Genetics Lab Testing Flyers

I have 5 flyers for another laboratory that I will be working with that need to have the logos and colors changed to match our laboratory, all of the information is correct its just changing of the format, logo and color scheme. I have attached 2 versions of our logo as well. (amber ridge diagnostics)

Target Market(s)

physician offices

Industry/Entity Type

Healthcare - Laboratoy

Colors
0054AA
0677BA
7BADD7
CADEEF
E8F1F8

Requirements
Must have
• all the information on the 5 current flyers
Should not have
• any mention of VantoCore

```html
<!DOCTYPE html>
<html lang="en">
<head>
<meta charset="utf-8">
<title>Amber Ridge Diagnostics – Genetic Carrier Screening</title>
<link href="https://fonts.googleapis.com/css2?family=Montserrat:wght@400;500;600;700&display=swap" rel="stylesheet">
<style>
:root{
  --blue-deep:#0054AA;
  --blue:#1F5FB2;
  --blue-mid:#0677BA;
  --blue-light:#7BADD7;
  --blue-pale:#B9D2EC;
  --blue-mist:#E8F1F8;
  --charcoal:#474747;
  --ink:#2b2b2b;
  --label:#555;
  --rule:#9a9a9a;
  --sign:#FFFF00;
  --canvas:#e4e4e4;
}
*{box-sizing:border-box;margin:0;padding:0}
html,body{width:1200px;height:982px;overflow:hidden}
body{background:var(--canvas);font-family:'Montserrat',sans-serif;color:var(--ink);position:relative}
.page{position:absolute;background:#fff;overflow:hidden;box-shadow:0 1px 4px rgba(0,0,0,.25)}
.page-left{left:14px;top:12px;width:580px;height:959px}
.page-right{left:606px;top:10px;width:581px;height:960px}
.corner{position:absolute;width:56px;height:56px;border-radius:50%;background:var(--blue)}
.corner.tl{left:-30px;top:-30px}
.corner.tr{right:-30px;top:-30px}

.brand{position:absolute;left:17px;top:10px;width:112px;text-align:center;color:var(--blue)}
.brand .mark{width:26px;height:26px;border-radius:50%;border:2px solid var(--blue);margin:0 auto 3px}
.brand .name{font-weight:700;font-size:11.5px;line-height:12px;letter-spacing:.2px}
.brand .sub{font-weight:700;font-size:6px;letter-spacing:3px;margin-top:2px}

.heading{position:absolute;text-align:center}
.heading .t1{color:var(--blue);font-size:12.5px;font-weight:500;letter-spacing:.4px}
.heading .t2{font-size:9.5px;font-weight:500;letter-spacing:.5px;margin-top:5px}
.heading .t3{font-size:6.5px;margin-top:5px}
.contact{position:absolute;font-size:6px;line-height:7.5px;color:#333}
.contact .row{display:flex;gap:5px;margin-bottom:6px;align-items:flex-start;border:none}
.contact svg{width:7px;height:7px;flex:none;margin-top:.5px}

.form{position:absolute;left:25px;top:76px;width:533px;height:873px;border:1px solid #555;display:flex;flex-direction:column;font-size:5.4px;color:var(--label)}
.bar{display:flex;align-items:center;color:#fff;font-weight:700;font-size:7.4px;letter-spacing:.3px;padding-left:8px;flex:none}
.bar small{font-size:4.4px;margin-left:6px}
.bar.dark{background:var(--charcoal)}
.bar.blue{background:var(--blue)}
.bar.center{justify-content:center;padding-left:0}
.bar.pale{background:var(--blue-pale);color:var(--ink);font-weight:500;font-size:5.2px;justify-content:center;padding-left:0}
.row{display:flex;flex:none;border-bottom:.6px solid var(--rule)}
.cell{border-right:.6px solid var(--rule);padding:9px 0 0 9px;text-transform:uppercase;white-space:nowrap}
.cell:last-child{border-right:none;flex:1}
.cell.mid{padding-top:0;display:flex;align-items:center}
.box{display:inline-block;width:4.5px;height:4.5px;border:.6px solid #777;margin-right:3px;vertical-align:-.5px;background:#fff}
.box.lg{width:7px;height:7px;flex:none}
.split{display:flex;flex:none}
.split>.half{flex:1;border-right:1px solid #fff}
.split>.half:last-child{border-right:none}
.checks{padding:5px 2px 0;display:flex;flex-wrap:wrap;gap:4px 6px;text-transform:uppercase;font-size:4.6px;height:27px;border-bottom:.6px solid var(--rule);white-space:nowrap}
.personal{display:flex;height:120px;flex:none;border-bottom:.6px solid var(--rule)}
.personal .col{flex:1;padding:8px 8px 0;border-right:.6px solid var(--rule);text-transform:uppercase;min-width:0}
.personal .col:last-child{border-right:none}
.pi-title{display:flex;align-items:center;font-size:4.9px;margin-bottom:9px;white-space:nowrap}
.pi-title small{font-size:2.8px;margin-left:4px}
.line{display:flex;align-items:center;font-size:4.3px;margin-bottom:7px}
.line span{width:38px}
.line i{flex:1;border-bottom:.6px solid #777}
.test-req{display:flex;height:37px;flex:none;border-bottom:.6px solid var(--rule)}
.test-req .lbl{width:74px;background:var(--charcoal);color:#fff;font-weight:700;font-size:7.4px;line-height:12px;padding:6px 8px}
.test-req .opts{flex:1;padding:6px 8px;font-size:4.9px;text-transform:uppercase;display:grid;grid-template-columns:200px 1fr;row-gap:10px;white-space:nowrap}
.icd-head{display:flex;height:20px;flex:none;background:var(--blue-pale);color:var(--ink);font-size:6.2px;font-weight:500}
.icd-head div{display:flex;align-items:center;padding-left:6px;border-right:.6px solid #fff}
.icd-body{display:flex;height:120px;flex:none;font-size:3.4px;line-height:6.1px;color:#444}
.icd-body .code{width:32px;padding:4px 0 0 5px;border-right:.6px solid var(--rule)}
.icd-body .desc{padding:4px 0 0 6px;border-right:.6px solid var(--rule)}
.icd-body .code div::before{content:"";display:inline-block;width:3px;height:3px;border:.5px solid #777;margin-right:3px;vertical-align:-.3px}
.icd-sub{background:var(--blue-pale);font-size:3.8px;text-align:center;color:var(--ink);padding:3px 0;margin:8px 0 6px}
.insurance{height:106px;flex:none;position:relative;font-size:4.3px;text-transform:uppercase}
.ins-line{position:absolute;display:flex;align-items:center;white-space:nowrap}
.ins-line i{display:inline-block;border-bottom:.6px solid #777;margin-left:3px}
.fine{position:absolute;font-size:3.2px;line-height:6.5px;color:#555;text-transform:none}
.sig{position:absolute;background:var(--sign)}
.sig-label{position:absolute;font-size:3.6px;color:#444}
.card-note{position:absolute;left:475px;top:32px;width:48px;height:58px;border:.6px solid #999;font-size:3.8px;line-height:6.5px;text-align:center;padding-top:8px;text-transform:none}
.consent-text{flex:1;position:relative;font-size:3.6px;line-height:6.6px;color:#444;padding:5px 8px}

.lab-heading .t1{font-size:12.5px}
.lab-heading .t3{font-size:6.5px;font-weight:600}
.lab-heading .t3 span{color:var(--blue);font-weight:500}
.dark-panel{position:absolute;left:16px;top:78px;width:274px;height:850px;background:var(--charcoal);color:#fff;overflow:hidden}
.light-panel{position:absolute;left:290px;top:78px;width:275px;height:850px;border:.8px solid #555;border-left:none}
.consent-title{position:absolute;left:11px;top:14px;font-size:11.4px;font-weight:700;line-height:16px;letter-spacing:.3px}
.pt-line{position:absolute;left:11px;font-size:7.5px;display:flex;align-items:center;gap:5px}
.pt-line i{display:inline-block;border-bottom:.6px solid #ccc}
.pt-line .box{border-color:#ddd;background:transparent;width:6px;height:6px}
.tab{position:absolute;display:flex;align-items:center;font-weight:700;font-size:11.4px;letter-spacing:.3px;white-space:nowrap}
.tab .icon{width:22px;height:22px;border-radius:50%;border:1.5px solid;display:flex;align-items:center;justify-content:center;margin-left:7px;flex:none}
.tab.white{background:#fff;color:var(--ink);padding-left:12px;height:23px}
.tab.white .icon{background:var(--charcoal);border-color:#fff;margin-right:-11px}
.tab.blue{background:var(--blue);color:#fff;padding-left:12px;height:23px;left:0}
.tab.blue .icon{background:#fff;border-color:var(--blue);margin-right:-11px}
.para{position:absolute;font-size:6.1px;line-height:12.9px}
.dark-panel .para{color:#eee;text-align:justify}
.light-panel .para{color:#333}
.numlist{position:absolute;left:10px;top:404px;width:258px;font-size:5.7px;line-height:11.6px;color:#eee}
.numlist li{list-style:none;display:flex;gap:11px;margin-bottom:6px}
.num{width:16px;height:16px;border-radius:50%;background:#fff;color:var(--ink);font-size:6.5px;display:flex;align-items:center;justify-content:center;flex:none;margin-top:2px}
.toplist{position:absolute;left:18px;top:12px;width:250px}
.toplist li{list-style:none;display:flex;gap:15px;margin-bottom:14px;font-size:3.9px;line-height:6.4px;color:#444}
.toplist .num{background:var(--charcoal);color:#fff}
.yn{position:absolute;font-size:6.4px;display:flex;align-items:center;gap:8px;color:#333}
</style>
</head>
<body>

<section class="page page-left">
  <div class="corner tl"></div><div class="corner tr"></div>
  <div class="brand"><div class="mark"></div><div class="name">AMBER RIDGE</div><div class="sub">DIAGNOSTICS</div></div>
  <div class="heading" style="left:150px;top:16px;width:300px">
    <div class="t1">GENETIC CARRIER SCREENING ANALYSIS</div>
    <div class="t2">CRESTLINE MOLECULAR DIAGNOSTICS, LLC</div>
    <div class="t3">Test Request Form and Statement of Medical Necessity</div>
  </div>
  <div class="contact" style="left:476px;top:17px">
    <div class="row"><svg viewBox="0 0 10 10"><path d="M2 1l2 2-1 1.5c.8 1.5 1.8 2.5 3.3 3.3L7.8 6.8l2 2-1.3 1.2C4.5 10 0 5.5 0 1.5z" fill="#333"/></svg>(555) 014 2290</div>
    <div class="row"><svg viewBox="0 0 10 10"><rect x="0" y="2" width="10" height="6.5" fill="#333"/><path d="M0 2l5 3.5L10 2" stroke="#fff" stroke-width=".8" fill="none"/></svg>support@amberridgedx.com</div>
    <div class="row"><svg viewBox="0 0 10 10"><path d="M5 0a3.6 3.6 0 0 0-3.6 3.6C1.4 6.4 5 10 5 10s3.6-3.6 3.6-6.4A3.6 3.6 0 0 0 5 0z" fill="#333"/><circle cx="5" cy="3.6" r="1.3" fill="#fff"/></svg><span>4120 Lakeview Pkwy,<br>Riverton, MI 48000</span></div>
  </div>

  <div class="form">
    <div class="split" style="height:21.5px">
      <div class="half bar blue">ORDERING &nbsp;PHYSICIAN</div>
      <div class="half bar blue">SEND RESULTS TO <small>(IF OTHER THAN ORDERING PHYSICIAN)</small></div>
    </div>
    <div class="row" style="height:37px">
      <div class="cell" style="width:199px">Name (Last, First, Degree)</div>
      <div class="cell" style="width:65px">NPI #</div>
      <div class="cell" style="width:197px">Name (Last, First, Degree)</div>
      <div class="cell">NPI #</div>
    </div>
    <div class="row" style="height:36px">
      <div class="cell" style="width:111px;padding-top:11px">Address</div>
      <div class="cell" style="width:39px;padding-top:11px">City</div>
      <div class="cell" style="width:57px;padding-top:10px">State</div>
      <div class="cell" style="width:57px;padding-top:11px">Zip</div>
      <div class="cell" style="width:109px;padding-top:11px">Address</div>
      <div class="cell" style="width:40px;padding-top:11px">City</div>
      <div class="cell" style="width:58px;padding-top:10px">State</div>
      <div class="cell" style="padding-top:11px">Zip</div>
    </div>
    <div class="row" style="height:29px">
      <div class="cell" style="width:111px">Office Phone</div>
      <div class="cell" style="width:39px">Fax</div>
      <div class="cell" style="width:114px;padding-top:8px">Email</div>
      <div class="cell" style="width:109px">Office Phone</div>
      <div class="cell" style="width:40px">Fax</div>
      <div class="cell" style="padding-top:8px">Email</div>
    </div>
    <div class="bar dark center" style="height:21.5px">PATIENT INFORMATION <small>(COMPLETE INFORMATION REQUIRED &nbsp;FOR INSURANCE COVERAGE)</small></div>
    <div class="row" style="height:28px">
      <div class="cell mid" style="width:199px">Patient Name (Last, First, Initial)</div>
      <div class="cell mid" style="width:45px;padding-left:6px"><span class="box"></span>Female</div>
      <div class="cell mid" style="width:55px;padding-left:14px"><span class="box"></span>Male</div>
      <div class="cell mid" style="width:89px">Birth &nbsp;Date (MM/DD/YY)</div>
      <div class="cell mid" style="width:72px">Phone</div>
      <div class="cell mid" style="padding-left:6px">Best Time to Call</div>
    </div>
    <div class="row" style="height:34px">
      <div class="cell mid" style="width:111px">Address</div>
      <div class="cell mid" style="width:39px">City</div>
      <div class="cell mid" style="width:57px;padding-bottom:3px">State</div>
      <div class="cell mid" style="width:45px">Zip</div>
      <div class="cell mid" style="padding-top:4px">Can we leave a detailed message at this number?<span style="margin-left:55px"><span class="box"></span>Yes &nbsp;&nbsp;<span class="box"></span>No</span></div>
    </div>
    <div class="bar dark" style="height:21.5px">ANCESTRY – CHECK ALL THAT APPLY <small>(COMPLETE INFORMATION REQUIRED &nbsp;FOR INSURANCE COVERAGE)</small></div>
    <div class="checks">
      <span><span class="box"></span>African</span><span><span class="box"></span>African American</span><span><span class="box"></span>Cajun</span><span><span class="box"></span>Caucasian</span><span><span class="box"></span>Dutch</span><span><span class="box"></span>French Canadian</span><span><span class="box"></span>Greek</span><span><span class="box"></span>Hungarian</span><span><span class="box"></span>Icelandic</span><span><span class="box"></span>Italian</span><span><span class="box"></span>Jewish, Ashkenaz</span>
      <span><span class="box"></span>Latin American/Caribbean</span><span><span class="box"></span>Mennonite</span><span><span class="box"></span>Middle Eastern/Mediterranean</span><span><span class="box"></span>Native American</span><span><span class="box"></span>Southeast Asian</span><span><span class="box"></span>Swedish</span><span><span class="box"></span>Adopted</span><span><span class="box"></span>Other <i style="display:inline-block;width:70px;border-bottom:.6px solid #777"></i></span>
    </div>
    <div class="bar dark" style="height:21.5px">INDICATION(S) FOR TESTING <small>INDICATE ALL THAT APPLY</small></div>
    <div class="row" style="height:27px">
      <div class="cell mid" style="width:208px;padding-left:2px"><span class="box"></span>General Reproductive Population – Family Planning</div>
      <div class="cell mid" style="width:134px;padding-left:12px"><span class="box"></span>Pregnant</div>
      <div class="cell mid" style="padding-left:9px"><span class="box"></span>Partner Pregnant</div>
    </div>
    <div class="bar dark" style="height:21px">PERSONAL INFORMATION</div>
    <div class="personal">
      <div class="col">
        <div class="pi-title"><span class="box lg" style="margin-right:5px"></span>Family History of Genetic Disease <small>(Include medical records and any test results if available)</small></div>
        <div class="line"><span>Relationship</span><i></i></div>
        <div class="line"><span>Disease</span><i></i></div>
        <div class="pi-title" style="margin-top:10px"><span class="box lg" style="margin-right:5px"></span>Family Member is a Known Carrier <small style="font-size:3.6px">(Family member is a known carrier)</small></div>
        <div class="line"><span>Relationship</span><i style="flex:none;width:90px;border:none"></i><span style="width:28px">Mutation</span><i></i></div>
        <div class="line"><span>Disease</span><i></i></div>
        <div style="font-size:4.8px;margin-top:13px">Unexplained Medical Conditions in Family</div>
      </div>
      <div class="col">
        <div class="pi-title"><span class="box lg" style="margin-right:5px"></span>Partner w/ Family History of Genetic Disease <small style="font-size:2.6px;margin-left:2px">Include medical records and any test results if available</small></div>
        <div class="line"><span style="width:55px">Relationship (to partner)</span><i></i></div>
        <div class="line"><span>Disease</span><i></i></div>
        <div class="pi-title" style="margin-top:10px"><span class="box lg" style="margin-right:5px"></span>Partner is a Known Carrier <small style="font-size:3.6px;margin-left:16px">(Include medical records)</small></div>
        <div class="line"><span style="width:26px">Disease</span><i></i></div>
        <div class="line"><span style="width:26px">Mutation</span><span style="width:60px;font-size:3.8px">(Attach clinical report)</span><i style="flex:none;width:80px"></i></div>
        <div style="font-size:4.8px;margin-top:13px">Partner's Ancestry and Ethnicity</div>
      </div>
    </div>
    <div class="test-req">
      <div class="lbl">TEST REQUESTED</div>
      <div class="opts">
        <span><span class="box"></span>Newborn Inherited Disease Screening – Expanded Test</span>
        <span><span class="box"></span>Include testing for Fragile-X (female patients only)</span>
        <span style="grid-column:1/3"><span class="box"></span>Custom (specific genes from Newborn panel) <i style="display:inline-block;width:200px;border-bottom:.6px solid #777"></i></span>
      </div>
    </div>
    <div class="bar blue center" style="height:20px">ICD10 CODES – COMMONLY USED CODES LISTED BELOW – INDICATE ALL RELEVANT CODES</div>
    <div class="icd-head">
      <div style="width:32px">ICD10</div><div style="width:232px">DESCRIPTION</div>
      <div style="width:50px">ICD10</div><div style="flex:1;border:none">DESCRIPTION</div>
    </div>
    <div class="icd-body">
      <div class="code"><div>Z13.0</div><div>Z13.228</div><div>Z31.440</div><div>Z31.441</div><div>Z13.79</div><div>Z15.89</div><div>Z81.0</div><div>Z34.01</div><div>Z34.02</div><div>Z34.03</div><div>Z34.80</div><div>Z84.81</div><div>Z81.8</div><div>Z81.8</div><div>Z81.8</div><div>Z81.8</div><div>Z81.8</div><div>Z83.2</div></div>
      <div class="desc" style="width:232px">
        <div>Encounter for screening for diseases of the blood and blood-forming organs and certain disorders</div><div>involving the immune mechanism</div><div>Encounter for screening for other metabolic disorders</div><div>Encounter of male for testing for genetic disease carrier status for procreative management</div><div>Encounter of female for testing for genetic disease carrier status for procreative management</div><div>Encounter for other screening for genetic and chromosomal anomalies</div><div>Genetic susceptibility to other disease</div><div>Family history of intellectual disabilities</div><div>Encounter for supervision of normal first pregnancy, first trimester</div><div>Encounter for supervision of normal first pregnancy, second trimester</div><div>Encounter for supervision of normal first pregnancy, third trimester</div><div>Encounter for supervision of other normal pregnancy, unspecified trimester</div><div>Family history of carrier of genetic disease</div><div>Family history of ADHD</div><div>Family history of Autism</div><div>Family history of Anxiety</div><div>Family history of Speech Impediments</div><div>Family history of Hyperactive Behavior</div><div>Family history of Sickle Cell Anemia</div>
      </div>
      <div style="flex:1;display:flex;flex-direction:column">
        <div style="display:flex"><div class="code" style="width:50px"><div>Z82.0</div><div>Z82.0</div><div>Z83.49</div><div>Z83.49</div><div>Z82.69</div></div>
          <div class="desc" style="flex:1;border:none"><div>Family history of Seizures</div><div>Family history of Spinal Muscular Atrophy</div><div>Family history of Cystic Fibrosis</div><div>Family history of Tay Sachs</div><div>Family history of other diseases of the musculoskeletal system and connective tissue</div></div></div>
        <div class="icd-sub">CORRESPONDING ICD-10 CODES BASED ON PATIENT'S PERSONAL AND FAMILY HISTORY</div>
        <div style="display:flex;flex:1"><div class="code" style="width:50px"><div>Z13.0</div><div>Z13.228</div><div>Z15.89</div><div>Z13.79</div></div>
          <div class="desc" style="flex:1;border:none"><div>Encounter for screening for diseases of the blood and blood-forming organs and certain disorders</div><div>involving the immune mechanism</div><div>Encounter for screening for other metabolic disorders</div><div>Genetic susceptibility to other disease</div><div>Encounter for other screening for genetic and chromosomal anomalies</div></div></div>
      </div>
    </div>
    <div class="bar blue center" style="height:21px">PAYMENT INFORMATION</div>
    <div class="bar pale" style="height:17px">OPTION 1: PLEASE BILL MY INSURANCE (requires patient signature and enlarged copy of both sides of insurance card(s). If two cards are submitted, indicate which is primary)</div>
    <div class="insurance">
      <div class="ins-line" style="left:6px;top:14px">Name of Policy Holder:<i style="width:150px"></i></div>
      <div class="ins-line" style="left:240px;top:14px">DOB:<i style="width:100px"></i></div>
      <div class="ins-line" style="left:358px;top:14px">Insurance Carrier:<i style="width:118px"></i></div>
      <div class="ins-line" style="left:6px;top:28px">Patient Relationship to Policy Holder: &nbsp;&nbsp;<span class="box"></span>Self &nbsp;&nbsp;<span class="box"></span>Spouse &nbsp;&nbsp;<span class="box"></span>Child &nbsp;&nbsp;<span class="box"></span>Other &nbsp;&nbsp;&nbsp;<span class="box"></span>Insurance ID #<i style="width:95px"></i></div>
      <div class="fine" style="left:6px;top:38px;width:460px">I hereby represent that I am covered by insurance and authorize Crestline Molecular Diagnostics, LLC to furnish my designated insurance carrier, health plan, or third party administrator the information on this form and other information provided by my healthcare provider necessary for reimbursement. I authorize Crestline Molecular Diagnostics, LLC to utilize a licensed third party laboratory for test processing when deemed necessary. I authorize Plan benefits to be payable to Crestline Molecular Diagnostics, LLC. If requested, I agree to assist Crestline Molecular Diagnostics, LLC in resolving insurance claim issues and if I do not assist, I may be responsible for the full test cost. I permit a copy of this authorization to be used in place of the original. I authorize Crestline Molecular Diagnostics, LLC to inform my plan of my test result ONLY if test results are required for reimbursement for testing or preauthorization of or payment for reflex/ additional testing.</div>
      <div class="card-note">Please include a copy of both sides of all insurance card(s)</div>
      <div class="sig" style="left:5px;top:76px;width:94px;height:21px"></div>
      <div class="sig" style="left:105px;top:76px;width:94px;height:21px"></div>
      <div class="sig-label" style="left:8px;top:100px">Patient / Responsible Party Signature</div>
      <div class="sig-label" style="left:107px;top:100px">Date</div>
    </div>
    <div class="bar pale" style="height:16px;font-size:5.4px">OPTION 2: PATIENT PAYMENT (Patient will be contacted for secure credit card information and to arrange payment plan)</div>
    <div class="bar blue center" style="height:16px;font-size:5.4px;font-weight:500">INFORMED CONSENT AND STATEMENT OF MEDICAL NECESSITY - TEST REQUESTS WITHOUT A SIGNATURE WILL NOT BE PROCESSED</div>
    <div class="consent-text">I have supplied information to the patient regarding genetic testing and the patient has given consent for genetic testing to be performed. I further confirm that this test is medically necessary for the diagnosis or detection of a disease, illness, impairment, symptom, syndrome or disorder, and the results will be used in the medical management and treatment decisions for the patient. The sample collection was done on the date indicated below unless otherwise noted. I confirm that the person listed in the Ordering Physician space above is authorized by law to order the test(s) requested herein.
      <div style="position:absolute;left:363px;top:38px;width:150px;border-bottom:.6px solid #777"></div>
      <div class="sig-label" style="left:364px;top:42px;font-size:4.2px">Medical Professional Signature</div>
      <div class="sig-label" style="left:449px;top:42px;font-size:4.2px">Date</div>
    </div>
  </div>
</section>

<section class="page page-right">
  <div class="corner tl"></div><div class="corner tr"></div>
  <div class="brand"><div class="mark"></div><div class="name">AMBER RIDGE</div><div class="sub">DIAGNOSTICS</div></div>
  <div class="heading lab-heading" style="left:150px;top:16px;width:300px">
    <div class="t1">AMBER RIDGE DIAGNOSTICS</div>
    <div class="t2">CRESTLINE MOLECULAR DIAGNOSTICS, LLC</div>
    <div class="t3">Marcus Ellery M.D., <span>Ph.D Laboratory Director</span></div>
  </div>
  <div class="contact" style="left:475px;top:17px">
    <div class="row"><svg viewBox="0 0 10 10"><path d="M2 1l2 2-1 1.5c.8 1.5 1.8 2.5 3.3 3.3L7.8 6.8l2 2-1.3 1.2C4.5 10 0 5.5 0 1.5z" fill="#333"/></svg>(555) 014 2290</div>
    <div class="row"><svg viewBox="0 0 10 10"><rect x="0" y="2" width="10" height="6.5" fill="#333"/><path d="M0 2l5 3.5L10 2" stroke="#fff" stroke-width=".8" fill="none"/></svg>support@amberridgedx.com</div>
    <div class="row"><svg viewBox="0 0 10 10"><path d="M5 0a3.6 3.6 0 0 0-3.6 3.6C1.4 6.4 5 10 5 10s3.6-3.6 3.6-6.4A3.6 3.6 0 0 0 5 0z" fill="#333"/><circle cx="5" cy="3.6" r="1.3" fill="#fff"/></svg><span>4120 Lakeview Pkwy,<br>Riverton, MI 48000</span></div>
  </div>

  <div class="dark-panel">
    <div class="consent-title">INFORMED CONSENT FOR GENETIC<br>CARRIER TESTING</div>
    <div class="pt-line" style="top:61px">Patient Name: <i style="width:175px;margin-left:4px"></i></div>
    <div class="pt-line" style="top:79px"><span class="box"></span>&nbsp;Amber Ridge Comprehensive Panel</div>
    <div class="pt-line" style="top:95px"><span class="box"></span>&nbsp;Custom <i style="width:172px"></i></div>

    <div class="tab white" style="left:0;top:121px;width:144px">INTRODUCTION <span class="icon"><svg width="10" height="10" viewBox="0 0 10 10"><circle cx="5" cy="4.3" r="2.4" fill="#fff"/><rect x="4" y="6.6" width="2" height="1.6" fill="#fff"/><path d="M5 0v1M1 4.3h1M8 4.3h1M2 1.5l.7.7M8 1.5l-.7.7" stroke="#fff" stroke-width=".6"/></svg></span></div>
    <div class="para" style="left:14px;top:149px;width:248px">I have discussed genetic testing with my doctor, an individual designated by my doctor or a genetics professional and understand the function and limitations of carrier screening testing and I am interested in obtaining genetic testing by submitting a biological sample of my own body fluids (such as saliva) blood or tissue. I may be pregnant at the time of this genetic test or not pregnant. This is a voluntary test to determine whether I have gene mutations that indicate that I am a carrier for one or more inherited diseases.</div>

    <div class="tab white" style="left:0;top:250px;width:263px;font-size:11px">TEST PURPOSE AND METHODOLOGY <span class="icon"><svg width="10" height="10" viewBox="0 0 10 10"><circle cx="5" cy="5" r="3.6" fill="none" stroke="#fff" stroke-width="1"/><circle cx="5" cy="5" r="1.4" fill="#fff"/></svg></span></div>
    <div class="para" style="left:14px;top:276px;width:250px;line-height:11.7px;text-align:left">The purpose of this molecular test is to determine whether I am a carrier for specific inherited diseases. I understand that as a carrier, I may not show any symptoms, but my children may be at significantly increased risk if the child's other parent is also a carrier for the same disease. I understand that the body fluid, blood or tissue specimen submitted is required for isolation and purification of DNA for molecular genetic testing. Crestline Molecular Diagnostics, LLC will analyze the DNA of a specific gene(s) to look for mutations associated with carrier status for these diseases</div>

    <div class="tab white" style="left:0;top:376px;width:130px">TEST RESULTS <span class="icon"><svg width="10" height="10" viewBox="0 0 10 10"><rect x="1.5" y="6" width="1.6" height="3" fill="#fff"/><rect x="4.2" y="4.5" width="1.6" height="4.5" fill="#fff"/><rect x="6.9" y="2.5" width="1.6" height="6.5" fill="#fff"/><path d="M1.5 4.5L5 2l3-1.5" stroke="#fff" stroke-width=".6" fill="none"/></svg></span></div>
    <ul class="numlist">
      <li><span class="num">1</span><span>I understand that screening does not detect all genetic carriers. I understand that testing negative means that the likelihood that I am a carrier for a genetic disease is reduced, but not eliminated.</span></li>
      <li><span class="num">2</span><span>I understand that one or more of the diseases on the panel may be passed in dominant fashion and may only be expressed later in life. I understand that this means that a positive test result for those diseases may have implications for my health or the health of my family</span></li>
      <li><span class="num">3</span><span>Should I test positive, it will be beneficial for my partner to be tested to better understand the risk of a relevant genetic disease in any offspring.</span></li>
      <li><span class="num">4</span><span>If I or my partner is a carrier, and the other is not, there is still a small possibility that a child will have a genetic disease.</span></li>
      <li><span class="num">5</span><span>If I and my partner are both carriers, I am aware that prenatal screening can be done to determine whether a child has inherited the genetic disease</span></li>
      <li><span class="num">6</span><span>I understand that results of this test will be evaluated in the context of personal and family history, ethnic information and other information. I have provided information as accurately as possible.</span></li>
      <li><span class="num">7</span><span>I understand the limitations of the results: the test could be based on probabilities, and may not provide 100% definitive conclusion regarding carrier status.</span></li>
      <li><span class="num">8</span><span>I understand that the molecular genetic test may not generate results and an additional sample may be needed to provide accurate results.</span></li>
      <li><span class="num">9</span><span>I understand that the molecular genetic test may not generate accurate results for many reasons, including but not limited to: sample mix-up, samples unavailable from critical family members, maternal contamination of prenatal samples, inaccurate reporting of family relationships, or technical problems.</span></li>
      <li><span class="num">10</span><span>I understand that only known positive mutations will be reported. Benign variants and variants of uncertain significance will not be reported.</span></li>
    </ul>
  </div>

  <div class="light-panel">
    <ul class="toplist">
      <li><span class="num">11</span><span>I understand that if I am female, I have the option of getting tested for Fragile X. I understand that results for Fragile X testing may be more complicated than results for diseases tested for as part of this test. I have spoken to my doctor about any concerns I may have regarding receiving testing for Fragile X and dealing with results.</span></li>
      <li><span class="num">12</span><span>I understand that genetic testing has implications for blood relatives. In consultation with an appropriate healthcare provider, I may wish to discuss sharing the test results with certain blood relatives who may be at risk. If I decide to do this, I should consider the best way to make this disclosure.</span></li>
      <li><span class="num">13</span><span>I understand that Crestline Molecular Diagnostics, LLC keeps test results confidential and is fully in compliance with all Health Insurance Portability and Accountability Act (HIPAA) regulations and Crestline Molecular Diagnostics, LLC will only release test results to my healthcare provider, his or her designee, or to another healthcare provider as directed by me (or a personal legally authorized to act on my behalf) in writing or otherwise as required by federal or state laws.</span></li>
      <li><span class="num">14</span><span>I understand Crestline Molecular Diagnostics, LLC reserves the right to: 1) Suggest additional molecular testing if it would help in resolving the patient's clinical genotyping, 2) report additional testing results (other than requested) if they are clinically relevant to me and my family, and refuse testing if one of the conditions in the Patient Consent is not met.</span></li>
    </ul>

    <div class="tab blue" style="top:171px;width:180px">USE OF SPECIMENS <span class="icon"><svg width="12" height="12" viewBox="0 0 12 12"><circle cx="6" cy="6" r="5" fill="var(--blue)"/><path d="M3.5 6.2l1.7 1.7 3.4-3.6" stroke="#fff" stroke-width="1.2" fill="none"/></svg></span></div>
    <div class="para" style="left:14px;top:200px;width:250px">After testing is completed, I understand that my blood, body fluid or tissue specimens may be disposed of or retained indefinitely for research, test validation, and/or education as long as my privacy is maintained. I understand that no compensation will be given nor will funds be forthcoming due to any invention(s) resulting from research and development using the specimens submitted. I understand that I may refuse to submit my specimen for use in this way and may withdraw my consent at any time by contacting the medical director. I understand that my refusal to consent to medical research will not affect my results. Indicate consent or denial below. If a box is not marked consent is implied</div>
    <div class="yn" style="left:17px;top:334px">Consent to the use of my sample for research: <span style="margin-left:8px"><span class="box" style="width:6px;height:6px"></span> Yes &nbsp;&nbsp;<span class="box" style="width:6px;height:6px"></span> No</span></div>

    <div class="tab blue" style="top:362px;width:180px">RECOMMENDATIONS <span class="icon"><svg width="12" height="12" viewBox="0 0 12 12"><circle cx="6" cy="6" r="5" fill="var(--blue)"/><path d="M3.5 6.2l1.7 1.7 3.4-3.6" stroke="#fff" stroke-width="1.2" fill="none"/></svg></span></div>
    <div class="para" style="left:14px;top:392px;width:250px">I understand that due to the dynamics of this field, there continues to be new information and data. It is recommended that I keep in contact with my healthcare provider, annually, to learn of any new developments in cancer genetics and to provide any updates to my personal or family history which may affect my cancer risks.</div>

    <div class="tab blue" style="top:471px;width:215px">FINANCIAL RESPONSIBILITY <span class="icon"><svg width="12" height="12" viewBox="0 0 12 12"><circle cx="6" cy="6" r="5" fill="var(--blue)"/><text x="6" y="8.4" font-size="7" text-anchor="middle" fill="#fff" font-family="Montserrat,sans-serif" font-weight="700">$</text></svg></span></div>
    <div class="para" style="left:10px;top:500px;width:258px;text-align:justify">Genetic testing of appropriate individuals is typically reimbursed by health insurance or covered by HMO's. I understand that I am responsible for any cost of the genetic test not reimbursed by insurance. I understand that if test cancellations are received prior to test set-up, processing will be honored at no charge. I understand that when requests for test cancellation are received after set-up, a cancellation report will be generated and a set-up fee will be charged. Once testing is initiated cancellation is not possible. I understand that I am responsible for all charges for testing and will be contacted for payment in the event my health plan does not reimburse for the test or CMD does not receive a response from my health plan in a reasonable length of time.</div>

    <div class="tab blue" style="top:634px;width:227px">PATIENT CONSENT STATEMENT <span class="icon"><svg width="12" height="12" viewBox="0 0 12 12"><rect x="3" y="2" width="6" height="8" fill="var(--blue)"/><path d="M4.3 4h3.4M4.3 6h3.4M4.3 8h3.4" stroke="#fff" stroke-width=".7"/></svg></span></div>
    <div class="para" style="left:10px;top:662px;width:258px;line-height:11.2px">By signing below, I, the patient having the test performed, acknowledge that:<br>I have read or have had read to me all of the above statements and understand the information regarding molecular genetics testing and have had the opportunity to ask questions I might have about the testing, the procedure, the risks, and the alternatives prior to my informed consent. I agree to have the molecular genetic testing. I consent to being tested to determine if I am a carrier for the diseases on the test selected and I will discuss the results and appropriate medical management with my healthcare provider/genetic counsellor. I am the owner of my medical history and test results. My healthcare practitioner should not discuss or disclose my test results and associated medical history to a third party, unless related to treatment or payment for treatment, without my express written authorization.</div>
    <div class="sig" style="left:10px;top:807px;width:94px;height:20px"></div>
    <div class="sig" style="left:110px;top:807px;width:94px;height:20px"></div>
    <div class="sig-label" style="left:13px;top:832px">Patient / Responsible Party Signature</div>
    <div class="sig-label" style="left:113px;top:832px">Date</div>
  </div>
</section>

</body>
</html>
```